Commercial Real Estate website

Need a web design commercial real estate company specializing in retail shopping centers based in Orlando, FL. We would like pictures of Orlando city skyline with hues and colors that go with hot pink. We want to stress the relationship of time on the value of real estate.
It should gave a rotating page that highlights our property listings.

Target Market(s)

Owners of shopping centers and national retail tenants looking for tenant representatives.

Industry/Entity Type

Real Estate

Number of Pages Required

5+ page

Font styles to use
Serif

Colors
e34197

Requirements
Must have
• Pictures of commercial retail grocery anchored shopping centers and city scapes and skylines.

```html
<!DOCTYPE html>
<html lang="en">
<head>
<meta charset="utf-8">
<title>Tidemark Commercial — Making Places Better</title>
<link href="https://fonts.googleapis.com/css2?family=Cinzel:wght@400;700&family=Playfair+Display:wght@400;700&family=Open+Sans:wght@400;600;700&display=swap" rel="stylesheet">
<style>
:root{
  --pink:#e34197;
  --pink-deep:#c72f80;
  --pink-soft:#f07bb9;
  --ink:#222;
  --char:#2c2c2e;
  --char-2:#3a3a3d;
  --grey:#8a8a8a;
  --light:#ededed;
  --white:#fff;
  --serif:'Playfair Display', Georgia, serif;
  --display:'Cinzel', 'Times New Roman', serif;
  --sans:'Open Sans', Arial, sans-serif;
}
*{box-sizing:border-box;margin:0;padding:0}
html,body{width:1200px;height:3212px;overflow:hidden}
body{font-family:var(--sans);color:var(--ink);background:var(--white);position:relative}
section,header,footer{position:absolute;left:0;width:1200px;overflow:hidden}
.btn{display:inline-block;font-family:var(--sans);font-size:11px;letter-spacing:1px;text-transform:uppercase;color:var(--white);border:1px solid var(--white);padding:6px 18px}
.btn--pink{background:var(--pink);border-color:var(--pink)}

/* Header + hero */
.hero{top:0;height:540px;background:#0b1730}
.hero__photo{position:absolute;inset:0;background:
  linear-gradient(180deg,#0d1b3a 0%,#1d3d72 38%,#3d6ea6 58%,#17294d 72%,#0a1226 100%)}
.hero__photo::after{content:"";position:absolute;left:0;right:0;top:250px;height:120px;
  background:linear-gradient(90deg,rgba(227,65,151,.15),rgba(255,190,120,.25),rgba(227,65,151,.15))}
.topbar{position:absolute;top:0;left:620px;width:560px;height:20px;background:var(--pink);color:var(--white);font-size:9px;display:flex;justify-content:space-around;align-items:center}
.nav{position:absolute;top:20px;left:0;width:1200px;height:110px;background:rgba(255,255,255,.96)}
.logo{position:absolute;left:40px;top:22px;display:flex;align-items:center;gap:8px;font-family:var(--serif);font-weight:700;font-size:28px;color:var(--pink)}
.logo__dot{width:16px;height:16px;border-radius:50%;background:var(--pink)}
.contact{position:absolute;left:760px;top:20px;display:flex;gap:28px;font-size:10px;color:#555}
.contact strong{display:block;color:var(--ink);font-size:11px}
.contact__item{display:flex;gap:8px;align-items:center}
.menu{position:absolute;left:300px;top:78px;display:flex;gap:20px;font-size:10px;letter-spacing:.8px;text-transform:uppercase;color:#444;list-style:none;white-space:nowrap}
.menu .is-active{color:var(--pink)}
.search{position:absolute;left:880px;top:72px;width:160px;height:24px;background:var(--pink);color:var(--white);font-size:10px;padding:5px 10px}
.hero__title{position:absolute;top:290px;width:100%;text-align:center;color:var(--white)}
.hero__title h1{font-family:var(--display);font-weight:400;font-size:44px;letter-spacing:4px}
.hero__title p{font-family:var(--display);font-size:16px;letter-spacing:3px;margin-top:4px}
.hero__caption{position:absolute;top:380px;width:100%;text-align:center;color:var(--white);font-family:var(--serif);font-size:15px;line-height:1.3}

/* About */
.about{top:540px;height:640px;background:linear-gradient(160deg,var(--char-2) 0%,var(--char) 60%,#252527 100%);color:#cfcfcf}
.about__text{position:absolute;left:60px;top:70px;width:360px}
.about h2,.expect h2{font-family:var(--serif);font-size:18px;color:var(--white);text-transform:uppercase;line-height:1.2}
.about h2 span{color:var(--pink)}
.about__text p{font-size:11px;line-height:1.7;margin-top:18px}
.about__photo{position:absolute;left:480px;top:180px;width:260px;height:220px;border:10px solid var(--pink);border-radius:44px;
  background:linear-gradient(180deg,#9cc3e6 0%,#cfe2f1 45%,#b58b6a 60%,#7a6a5c 100%)}
.about__cap{position:absolute;left:480px;top:412px;width:260px;text-align:center;font-size:10px;color:var(--pink)}
.expect{position:absolute;left:750px;top:70px;width:380px}
.expect__item{display:flex;gap:14px;margin-top:32px}
.expect__icon{flex:none;width:32px;height:32px}
.expect__item h3{font-family:var(--serif);font-size:13px;color:var(--pink);text-transform:uppercase}
.expect__item p{font-size:10.5px;line-height:1.6;margin-top:6px}

/* Listings */
.listings{top:1180px;height:640px;background:var(--white)}
.listings__side{position:absolute;left:0;top:0;width:480px;height:640px;background:linear-gradient(180deg,var(--pink) 0%,var(--pink-deep) 100%);color:var(--white)}
.listings__side .tag{position:absolute;left:268px;font-family:var(--serif);font-size:36px;line-height:1;text-transform:uppercase}
.listings__side .featured{position:absolute;left:268px;top:300px;font-family:var(--serif);font-size:22px;line-height:1.2;text-transform:uppercase}
.cards{position:absolute;left:500px;top:60px;display:grid;grid-template-columns:repeat(3,150px);column-gap:18px;row-gap:40px}
.card__photo{width:120px;height:120px;border:6px solid var(--char);border-radius:26px;margin:0 auto}
.card--pink .card__photo{border-color:var(--pink)}
.card h4{font-family:var(--serif);font-size:10px;text-align:center;margin-top:10px;line-height:1.3}
.card p{font-size:9px;color:var(--grey);text-align:center;line-height:1.5;margin-top:6px}
.card a{display:block;font-size:8px;text-transform:uppercase;color:var(--pink);text-align:center;margin-top:6px;letter-spacing:1px}

/* News band */
.news{top:1820px;height:320px}
.news__photo{position:absolute;inset:0;background:linear-gradient(90deg,#b9a292 0%,#d9cbbd 40%,#cdbba8 70%,#a48e7c 100%)}
.news__box{position:absolute;left:250px;top:50px;width:700px;height:220px;background:rgba(227,65,151,.92);color:var(--white);text-align:center;padding:26px 60px}
.news__box h2{font-family:var(--serif);font-size:22px;font-weight:400}
.news__quote{font-family:var(--serif);font-size:36px;line-height:.8;margin-top:10px}
.news__box p{font-size:12px;line-height:1.6}
.news__box .btn{margin-top:16px}

/* Gallery */
.gallery{top:2140px;height:640px;background:linear-gradient(180deg,#4a4a4a 0%,#2e2e2e 100%)}
.gallery__bg{position:absolute;inset:0;background:linear-gradient(180deg,rgba(120,120,120,.35),rgba(40,40,40,.2))}
.gallery h2{position:absolute;top:78px;width:100%;text-align:center;font-family:var(--serif);font-size:18px;color:var(--white);letter-spacing:2px}
.gallery h2 small{display:block;font-family:var(--sans);font-size:10px;color:#bbb;letter-spacing:1px;margin-top:4px}
.gallery__arrow{position:absolute;top:86px;width:26px;height:26px;border-radius:50%;background:var(--white)}
.gallery__grid{position:absolute;left:272px;top:192px;display:grid;grid-template-columns:repeat(3,200px);gap:40px 28px}
.shot{height:132px;border:4px solid var(--white);border-radius:10px}

/* Footer */
.footer{top:2780px;height:432px;background:linear-gradient(180deg,#f4f4f4 0%,#dedede 100%)}
.footer__skyline{position:absolute;left:0;bottom:0;width:1200px;height:300px;background:linear-gradient(180deg,rgba(180,180,180,0) 0%,rgba(160,160,160,.45) 60%,rgba(140,140,140,.6) 100%)}
.cta{position:absolute;top:28px;width:100%;text-align:center}
.cta h2{font-family:var(--serif);font-size:16px;text-transform:uppercase;letter-spacing:1px}
.cta .btn{margin-top:12px}
.footer .logo{top:150px;left:80px}
.footer__about{position:absolute;left:80px;top:200px;width:200px;font-size:9.5px;line-height:1.6;color:#555}
.footer__col{position:absolute;top:150px;font-size:10px;line-height:1.9;color:#444}
.footer__col h3{font-family:var(--serif);font-size:12px;text-transform:uppercase;color:var(--pink);margin-bottom:6px}
.social{position:absolute;left:720px;top:150px;display:flex;gap:8px}
.social span{width:26px;height:26px;border-radius:50%;background:var(--pink)}
.footer__phone{position:absolute;left:720px;top:190px;font-family:var(--serif);font-size:14px;color:var(--pink)}
.footer__touch{position:absolute;left:720px;top:222px}
</style>
</head>
<body>

<header class="hero">
  <div class="hero__photo" role="img" aria-label="Orlando city skyline at dusk reflected on the lake"></div>
  <div class="topbar"><span>hello@tidemarkretail.com</span><span>(407) 555-0148</span><span>Orlando, FL</span></div>
  <nav class="nav">
    <div class="logo"><span class="logo__dot"></span>Tidemark</div>
    <div class="contact">
      <div class="contact__item">
        <svg width="20" height="20" viewBox="0 0 20 20"><circle cx="10" cy="10" r="9" fill="none" stroke="#e34197" stroke-width="1.5"/><path d="M5 7h10v6H5z M5 7l5 4 5-4" fill="none" stroke="#e34197" stroke-width="1.2"/></svg>
        <div><strong>Email Us</strong>hello@tidemarkretail.com</div>
      </div>
      <div class="contact__item">
        <svg width="20" height="20" viewBox="0 0 20 20"><circle cx="10" cy="10" r="9" fill="none" stroke="#e34197" stroke-width="1.5"/><path d="M7 5l2 3-1 1a6 6 0 0 0 3 3l1-1 3 2-1 2c-4 0-8-4-8-8z" fill="#e34197"/></svg>
        <div><strong>Contact by Phone</strong>(407) 555-0148</div>
      </div>
    </div>
    <ul class="menu">
      <li class="is-active">Home</li><li>Our Services</li><li>Property Listings</li><li>Tenants</li><li>News</li><li>Contact Us</li>
    </ul>
    <div class="search">Search</div>
  </nav>
  <div class="hero__title">
    <h1>· Making Places · Better ·</h1>
    <p>Communities | Shopping Centers | Retailers</p>
  </div>
  <div class="hero__caption">Orlando City Skyline<br>OCTOBER 2015</div>
</header>

<section class="about">
  <div class="about__text">
    <h2>About <span>Tidemark</span><br>Commercial</h2>
    <p>Tidemark Commercial is an Orlando firm focused on grocery anchored shopping centers. We guide owners and national tenants through every stage of a deal, because time shapes the value of every property we touch.</p>
    <p>Our team pairs local market study with careful leasing plans, helping centers fill faster and hold their worth over the long run for owners and retailers.</p>
    <p>Read more about our story</p>
  </div>
  <div class="about__photo" role="img" aria-label="Photo of a grocery anchored shopping center storefront"></div>
  <div class="about__cap">Lakeside Grove Shopping Center<br>Winter Park, Florida</div>
  <div class="expect">
    <h2>What you can expect<br>from the summit</h2>
    <div class="expect__item">
      <svg class="expect__icon" viewBox="0 0 32 32"><circle cx="16" cy="16" r="16" fill="#e34197"/><path d="M13 10l7 6-7 6" fill="none" stroke="#fff" stroke-width="2"/></svg>
      <div><h3>Communities</h3><p>We study each trade area so new centers serve the people who live close by and return week after week.</p></div>
    </div>
    <div class="expect__item">
      <svg class="expect__icon" viewBox="0 0 32 32"><circle cx="16" cy="16" r="16" fill="#e34197"/><path d="M13 10l7 6-7 6" fill="none" stroke="#fff" stroke-width="2"/></svg>
      <div><h3>Shopping Centers</h3><p>Leasing, sales and repositioning plans built to lift income and keep anchors strong for years ahead.</p></div>
    </div>
    <div class="expect__item">
      <svg class="expect__icon" viewBox="0 0 32 32"><circle cx="16" cy="16" r="16" fill="#e34197"/><path d="M13 10l7 6-7 6" fill="none" stroke="#fff" stroke-width="2"/></svg>
      <div><h3>Retailers</h3><p>Tenant representation that finds the right site and terms for national brands entering Florida.</p></div>
    </div>
  </div>
</section>

<section class="listings">
  <div class="listings__side" role="img" aria-label="Pink-toned photo of a retail plaza">
    <div class="tag" style="top:120px">For<br>Lease</div>
    <span class="btn" style="position:absolute;left:268px;top:200px">View All</span>
    <div class="featured">Featured<br>Listings</div>
    <div class="tag" style="top:400px">For<br>Sale</div>
    <span class="btn" style="position:absolute;left:268px;top:480px">View All</span>
  </div>
  <div class="cards">
    <div class="card"><div class="card__photo" style="background:linear-gradient(180deg,#8fb6dc,#c9b59a)" role="img" aria-label="Shopping center photo"></div><h4>Oak Ridge Marketplace<br>Retail Space</h4><p>1200 sq ft inline space<br>Orlando, FL 32801</p><a>View Details</a></div>
    <div class="card"><div class="card__photo" style="background:linear-gradient(180deg,#a4c4e2,#b09478)" role="img" aria-label="Shopping center photo"></div><h4>Conway Village Plaza<br>Retail Space</h4><p>2400 sq ft end cap<br>Orlando, FL 32812</p><a>View Details</a></div>
    <div class="card"><div class="card__photo" style="background:linear-gradient(180deg,#9cbfe0,#c7a27a)" role="img" aria-label="Shopping center photo"></div><h4>Baldwin Commons<br>Retail Space</h4><p>1800 sq ft inline space<br>Orlando, FL 32814</p><a>View Details</a></div>
    <div class="card card--pink"><div class="card__photo" style="background:linear-gradient(180deg,#6fa7de,#d8c3a4)" role="img" aria-label="Shopping center photo"></div><h4>Sand Lake Crossing<br>Center For Sale</h4><p>84,000 sq ft center<br>Orlando, FL 32819</p><a>View Details</a></div>
    <div class="card card--pink"><div class="card__photo" style="background:linear-gradient(180deg,#a9c9e6,#c09a74)" role="img" aria-label="Shopping center photo"></div><h4>Lee Road Square<br>Center For Sale</h4><p>62,500 sq ft center<br>Winter Park, FL 32789</p><a>View Details</a></div>
    <div class="card card--pink"><div class="card__photo" style="background:linear-gradient(180deg,#93bbe0,#b58d6b)" role="img" aria-label="Shopping center photo"></div><h4>Kissimmee Town Center<br>Center For Sale</h4><p>97,300 sq ft center<br>Kissimmee, FL 34741</p><a>View Details</a></div>
  </div>
</section>

<section class="news">
  <div class="news__photo" role="img" aria-label="Photo of a smiling older couple"></div>
  <div class="news__box">
    <h2>Palm Beach Retail in the Fifth Year Recovery</h2>
    <div class="news__quote">“</div>
    <p>The Palm Beach market has held in the fifth year of a recovery, reporting 92% retail occupancy levels and 75% of its center sales now move fast across the county.</p>
    <span class="btn">Continue Reading</span>
  </div>
</section>

<section class="gallery">
  <div class="gallery__bg" role="img" aria-label="Faded photo of a shopping mall interior"></div>
  <h2>GALLERY<small>Our Centers</small></h2>
  <svg class="gallery__arrow" style="left:272px" viewBox="0 0 26 26"><circle cx="13" cy="13" r="13" fill="#fff"/><path d="M15 8l-5 5 5 5" fill="none" stroke="#333" stroke-width="2"/></svg>
  <svg class="gallery__arrow" style="left:902px" viewBox="0 0 26 26"><circle cx="13" cy="13" r="13" fill="#fff"/><path d="M11 8l5 5-5 5" fill="none" stroke="#333" stroke-width="2"/></svg>
  <div class="gallery__grid">
    <div class="shot" style="background:linear-gradient(180deg,#c64a2c,#e0a35a)" role="img" aria-label="Market storefront"></div>
    <div class="shot" style="background:linear-gradient(180deg,#4f86c6,#b65a3e)" role="img" aria-label="Shopping plaza building"></div>
    <div class="shot" style="background:linear-gradient(180deg,#d0b089,#8a6a4c)" role="img" aria-label="Retail arcade"></div>
    <div class="shot" style="background:linear-gradient(180deg,#6a5040,#c49a6a)" role="img" aria-label="Fountain in a shopping court"></div>
    <div class="shot" style="background:linear-gradient(180deg,#e08a4e,#a8583a)" role="img" aria-label="Shops at sunset"></div>
    <div class="shot" style="background:linear-gradient(180deg,#8aa3b8,#5c6470)" role="img" aria-label="Center entrance"></div>
  </div>
</section>

<footer class="footer">
  <div class="footer__skyline" role="img" aria-label="Faint grey city skyline"></div>
  <div class="cta"><h2>Ready to talk about your next investment?</h2><span class="btn btn--pink">Contact Us Today</span></div>
  <div class="logo"><span class="logo__dot"></span>Tidemark</div>
  <p class="footer__about">Retail real estate advisors serving owners and tenants across Central Florida.</p>
  <div class="footer__col" style="left:350px"><h3>Quick Links</h3>Home<br>Our Services<br>Property Listings<br>Tenants<br>Contact Us</div>
  <div class="footer__col" style="left:520px"><h3>Contact</h3>400 Lake Shore Avenue<br>Suite 210<br>Orlando, FL 32801<br>hello@tidemarkretail.com</div>
  <div class="social"><span></span><span></span><span></span><span></span><span></span></div>
  <div class="footer__phone">(407) 555-0148</div>
  <span class="btn btn--pink footer__touch">Get in Touch</span>
</footer>

</body>
</html>
```